Business Cards for a law firm

Business cards for our law firm. Use our silhoette logo and OAK HARBOR - check our website (www.oakharbor-legal.com)

Contact Information for Business Card

our silhouette logo, OAK HARBOR, 800-555-0147, Dorian Kestrup, dorian@oakharbor-legal.com

Requirements
Must have
• our silhouette logo, OAK HARBOR, 800-555-0147, Dorian Kestrup, dorian@oakharbor-legal.com

```html
<!DOCTYPE html>
<html lang="en">
<head>
<meta charset="utf-8">
<title>Oak Harbor – Business Cards</title>
<link rel="stylesheet" href="https://fonts.googleapis.com/css2?family=Questrial&display=swap">
<style>
  :root {
    --navy: #22336b;
    --orange: #f5a623;
    --white: #ffffff;
    --backdrop: #e4e4e9;
    --divider: #dfe2ea;
  }
  * { margin: 0; padding: 0; box-sizing: border-box; }
  html, body { width: 1200px; height: 1200px; overflow: hidden; }
  body {
    background: var(--backdrop);
    font-family: "Questrial", sans-serif;
    position: relative;
  }
  .card {
    position: absolute;
    left: 232px;
    width: 763px;
    height: 436px;
    border-radius: 44px;
    overflow: hidden;
  }
  .card-front { top: 107px; background: var(--white); }
  .card-back { top: 649px; background: var(--navy); }

  /* front */
  .front-brand { position: absolute; left: 80px; top: 64px; height: 86px; display: flex; align-items: center; gap: 14px; }
  .brand-square { width: 52px; height: 52px; background: var(--navy); }
  .brand-name {
    font-size: 56px; color: var(--navy); letter-spacing: 2px; line-height: 1; white-space: nowrap;
  }
  .front-rule { position: absolute; left: 0; right: 0; top: 193px; height: 6px; background: var(--navy); }

  .person { position: absolute; right: 433px; top: 262px; text-align: right; }
  .person-name { font-size: 35px; line-height: 1; color: var(--navy); white-space: nowrap; }
  .person-name .first { color: var(--orange); }
  .person-title { font-size: 15px; color: var(--orange); margin-top: 10px; }

  .split {
    position: absolute; left: 350px; top: 236px; width: 2px; height: 160px;
    background: linear-gradient(to bottom, transparent, var(--divider) 20%, var(--divider) 80%, transparent);
  }

  .contact-track { position: absolute; left: 388px; top: 270px; width: 4px; height: 96px; background: #3a3a3a; }
  .icon {
    position: absolute; width: 36px; height: 36px; border-radius: 7px;
    display: flex; align-items: center; justify-content: center;
  }
  .icon svg { width: 18px; height: 18px; }
  .icon-navy { background: var(--navy); }
  .icon-orange { background: var(--orange); }
  .icon-phone { left: 372px; top: 248px; }
  .icon-web { left: 372px; top: 297px; }
  .icon-pin { left: 372px; top: 350px; }

  .contact-text {
    position: absolute; left: 427px; font-size: 17.5px; line-height: 21px; color: var(--navy); white-space: nowrap;
  }
  .contact-phone { top: 256px; }
  .contact-online { top: 295px; }
  .contact-address { top: 347px; }

  /* back */
  .back-brand { position: absolute; left: 177px; top: 138px; display: flex; align-items: center; gap: 18px; }
  .back-brand .brand-square { width: 96px; height: 96px; background: var(--white); }
  .back-name { color: var(--white); font-size: 60px; line-height: 0.9; letter-spacing: 2px; }
  .back-web { position: absolute; left: 228px; top: 304px; display: flex; align-items: center; gap: 19px; }
  .back-web .icon { position: static; width: 37px; height: 37px; }
  .back-web span { color: var(--white); font-size: 17.5px; }
</style>
</head>
<body>

<section class="card card-front" aria-label="Business card front">
  <div class="front-brand">
    <div class="brand-square"></div>
    <div class="brand-name">OAK HARBOR</div>
  </div>
  <div class="front-rule"></div>

  <div class="person">
    <div class="person-name"><span class="first">Dorian</span> Kestrup</div>
    <div class="person-title">Founder/Director</div>
  </div>

  <div class="split"></div>

  <div class="contact-track"></div>
  <div class="icon icon-navy icon-phone">
    <svg viewBox="0 0 24 24" fill="#fff"><path d="M6.6 10.8a15 15 0 0 0 6.6 6.6l2.2-2.2c.3-.3.7-.4 1-.2 1.1.4 2.3.6 3.6.6.6 0 1 .4 1 1V20c0 .6-.4 1-1 1A17 17 0 0 1 3 4c0-.6.4-1 1-1h3.5c.6 0 1 .4 1 1 0 1.3.2 2.5.6 3.6.1.3 0 .7-.2 1z"/></svg>
  </div>
  <div class="icon icon-orange icon-web">
    <svg viewBox="0 0 24 24" fill="none" stroke="#fff" stroke-width="2"><circle cx="12" cy="12" r="9"/><path d="M3 12h18M12 3c3 3 3 15 0 18M12 3c-3 3-3 15 0 18"/></svg>
  </div>
  <div class="icon icon-navy icon-pin">
    <svg viewBox="0 0 24 24" fill="#fff"><path d="M12 2a7 7 0 0 0-7 7c0 5 7 13 7 13s7-8 7-13a7 7 0 0 0-7-7zm0 9.5A2.5 2.5 0 1 1 12 6.5a2.5 2.5 0 0 1 0 5z"/></svg>
  </div>

  <div class="contact-text contact-phone">800-555-0147</div>
  <div class="contact-text contact-online">dorian@oakharbor-legal.com<br>www.oakharbor-legal.com</div>
  <div class="contact-text contact-address">La, Street<br>Location</div>
</section>

<section class="card card-back" aria-label="Business card back">
  <div class="back-brand">
    <div class="brand-square"></div>
    <div class="back-name">OAK<br>HARBOR</div>
  </div>
  <div class="back-web">
    <div class="icon icon-orange">
      <svg viewBox="0 0 24 24" fill="none" stroke="#fff" stroke-width="2"><circle cx="12" cy="12" r="9"/><path d="M3 12h18M12 3c3 3 3 15 0 18M12 3c-3 3-3 15 0 18"/></svg>
    </div>
    <span>www.oakharbor-legal.com</span>
  </div>
</section>

</body>
</html>
```